Marlowvale Wholefoods web design

Go to marlowvalewholefoods.com.au an using the current layout create a design that will attract customers to this wholefood website.

You may suggest / make slight changes to the layout to create effective graphic design principles.

The LOGO design is TM already. So no changes there. Second logo attached is authorised for use and is a area branding LOGO.

Colours need to reflect health and wellbeing.

Don't want Medical style or New age.
Updates

Thank you for your submissions so far. I have sent them out to a trusty panel of friends to hear what they have to say. Some of you have done very well.

Reason: There are a few submissions outstanding. I will eliminate a few designs today and give feed back. Thankyou

Thank you for your submissions so far I will not be asking for more design submissions from other designers. The ones I have are under consideration and there are a few minor changes to each that may just bring out the one that is IT! The two designs I have narrowed it down to are very different in approach so please bear with me a couple more days. Thank you.

Target Market(s)

Whole food health concious people target market locally Home Delivery would be young Mums with restricted movement because of young children. Older people that are restricted transport users.

Busy commuters that leave our area for work and just want to relax on the weekend with their family and local bush walking or garden activities.

Industry/Entity Type

Graphic Design

Requirements
Should not have
• Medical or sterile hospital feel. New age or too alternative living feel.

```html
<!DOCTYPE html>
<html lang="en">
<head>
<meta charset="utf-8">
<title>Marlowvale Wholefoods</title>
<link href="https://fonts.googleapis.com/css2?family=Open+Sans:wght@400;600;700&display=swap" rel="stylesheet">
<style>
:root{
  --purple:#6a1d6c;
  --purple-dark:#4f1451;
  --green:#7c9b2c;
  --green-dark:#5f7c1c;
  --ink:#333333;
  --muted:#777777;
  --line:#dddddd;
  --panel:#3f3f3f;
  --price:#c0392b;
  --white:#ffffff;
}
*{box-sizing:border-box;margin:0;padding:0}
html,body{width:1200px;height:2236px;overflow:hidden}
body{font-family:"Open Sans",Arial,sans-serif;color:var(--ink);background:var(--white);font-size:13px}
.wrap{width:960px;margin:0 auto;position:relative}
a{color:inherit;text-decoration:none}

.topbar{height:32px;background:var(--purple);color:var(--white);font-size:12px}
.topbar .wrap{display:flex;justify-content:space-between;align-items:center;height:32px}
.topbar .contact{display:flex;gap:22px;align-items:center}
.topbar .contact span{display:flex;gap:6px;align-items:center}

.header{height:116px}
.header .wrap{height:116px}
.logo{position:absolute;left:0;top:12px;width:240px;height:92px;display:flex;align-items:center;gap:10px}
.logo .dot{width:28px;height:28px;border-radius:50%;background:var(--green)}
.logo .name{font-weight:700;font-size:20px;color:var(--purple);line-height:1.1}
.account{position:absolute;right:0;top:5px;width:300px;font-size:10px}
.account .row{display:flex;gap:6px;justify-content:flex-end;align-items:center;margin-bottom:3px;height:16px}
.input{border:1px solid var(--line);height:16px;width:130px;background:#fafafa}
.btn-reg{background:var(--purple);color:var(--white);padding:1px 14px;font-size:10px;font-weight:600;line-height:14px}
.account .forgot{text-align:right;color:var(--muted);font-size:10px;line-height:12px}
.nav{position:absolute;left:270px;right:0;bottom:6px;height:34px;background:var(--green);display:flex;align-items:center;padding:0 24px;gap:32px;color:var(--white);font-weight:600;font-size:12px;text-transform:uppercase}
.nav .search{margin-left:auto;width:18px;height:18px}

.hero{height:360px;position:relative;background:linear-gradient(180deg,#9fc4e4 0%,#cfe0ea 45%,#b7c98a 75%,#7f9d3c 100%)}
.hero-photo{position:absolute;right:80px;top:20px;width:520px;height:340px;background:radial-gradient(ellipse at 50% 40%,#e8dcc5 0%,#c9b38f 40%,rgba(160,150,110,0) 75%)}
.hero .copy{position:absolute;left:220px;top:100px;width:280px;color:var(--white)}
.hero h1{font-size:40px;line-height:1.05;font-weight:700;text-shadow:0 1px 3px rgba(0,0,0,.3)}
.hero p{font-size:12px;margin:12px 0 16px;line-height:1.5}
.btn-green{display:inline-block;background:var(--green);color:var(--white);font-size:12px;font-weight:600;padding:7px 18px}
.arrow{position:absolute;top:160px;width:30px;height:30px;border-radius:50%}
.arrow.l{left:10px}.arrow.r{right:10px}

.section-title{font-size:22px;font-weight:700;color:var(--ink);text-transform:uppercase;padding-bottom:8px;border-bottom:2px solid var(--line);position:relative}
.section-title::after{content:"";position:absolute;left:0;bottom:-2px;width:120px;height:2px;background:var(--green)}

.deals{padding-top:30px;height:370px}
.products{display:flex;justify-content:space-between;margin-top:20px}
.product{width:210px;text-align:center}
.product .shot{height:130px;width:170px;margin:0 auto 10px}
.product h3{font-size:12px;font-weight:700;text-transform:uppercase}
.product .price{color:var(--price);font-weight:700;font-size:14px;margin:2px 0}
.product .desc{font-size:10px;color:var(--muted);line-height:1.4}
.product .more{display:inline-block;margin-top:8px;background:var(--green);color:var(--white);font-size:11px;padding:4px 14px}

.main{display:flex;justify-content:space-between;height:700px}
.news{width:660px}
.news-item{display:flex;justify-content:space-between;border-bottom:1px solid var(--line);padding:14px 0;height:126px}
.news-item .text{width:520px}
.news-item h3{font-size:17px;font-weight:600;color:var(--ink)}
.news-item p{font-size:11px;color:var(--muted);line-height:1.5;margin:4px 0}
.news-item .read{font-size:11px;color:var(--green);font-weight:600}
.news-item .thumb{width:90px;height:90px}
.sidebar{width:250px}
.side-title{font-size:16px;font-weight:600;padding-bottom:5px;border-bottom:2px solid var(--green);margin-bottom:5px}
.cat{border:1px solid var(--line);font-size:10px;margin-bottom:14px}
.cat li{list-style:none;padding:1px 10px;line-height:14px;border-bottom:1px solid #eeeeee;color:#555}
.cat li.head{background:#f2f2f2;font-weight:600}

.testimonial{height:200px;margin-top:10px;display:flex;align-items:flex-end}
.testimonial .person{width:230px;height:200px;background:linear-gradient(180deg,#e9e6e1 0%,#bdb3a8 60%,#4a4a4a 100%)}
.testimonial .quote{flex:1;height:170px;background:var(--panel);color:#e8e8e8;padding:36px 80px;font-size:13px;line-height:1.7;position:relative}
.testimonial .qm{position:absolute;color:var(--white);font-size:60px;font-weight:700;line-height:1}
.qm.open{left:28px;top:18px}.qm.close{right:28px;bottom:-10px}

.footer{position:absolute;left:0;right:0;top:1840px;height:350px;background:var(--green);color:var(--white)}
.footer .wrap{display:flex;justify-content:space-between;padding-top:30px}
.fcol{width:220px}
.fcol h4{font-size:18px;font-weight:600;padding-bottom:8px;border-bottom:1px solid rgba(255,255,255,.5);margin-bottom:10px}
.fcol li{list-style:none;font-size:11px;line-height:1.9}
.fcol label{display:block;font-size:11px;margin-top:6px}
.fcol .field{height:24px;background:var(--white);margin-top:3px}
.btn-sub{display:inline-block;margin-top:12px;background:var(--purple);color:var(--white);font-size:12px;padding:5px 20px}
.bottombar{position:absolute;left:0;right:0;top:2190px;height:46px;background:var(--purple);color:var(--white);font-size:11px}
.bottombar .wrap{line-height:46px}
</style>
</head>
<body>

<div class="topbar">
  <div class="wrap">
    <div>My Account &nbsp;|&nbsp; Shopping cart &nbsp;|&nbsp; Checkout &nbsp;|&nbsp; Login</div>
    <div class="contact">
      <span><svg width="12" height="12" viewBox="0 0 24 24"><path fill="#fff" d="M6.6 10.8a15 15 0 006.6 6.6l2.2-2.2c.3-.3.7-.4 1-.2 1.1.4 2.3.6 3.6.6.6 0 1 .4 1 1V20c0 .6-.4 1-1 1A17 17 0 013 4c0-.6.4-1 1-1h3.5c.6 0 1 .4 1 1 0 1.3.2 2.5.6 3.6.1.3 0 .7-.2 1z"/></svg>(02) 5550 1234</span>
      <span><svg width="13" height="10" viewBox="0 0 26 20"><rect x="1" y="1" width="24" height="18" fill="none" stroke="#fff" stroke-width="2"/><path d="M1 1l12 10L25 1" fill="none" stroke="#fff" stroke-width="2"/></svg>mail@marlowvalewholefoods.com.au</span>
    </div>
  </div>
</div>

<header class="header">
  <div class="wrap">
    <div class="logo"><span class="dot"></span><span class="name">Marlowvale<br>Wholefoods</span></div>
    <div class="account">
      <div class="row"><span class="btn-reg">Register</span></div>
      <div class="row"><span class="input"></span><span class="input" style="width:100px"></span></div>
      <div class="row">Remember me &nbsp; <span class="btn-reg" style="padding:1px 10px">Login</span></div>
      <div class="forgot">Forgot Your Password?</div>
    </div>
    <nav class="nav">
      <a>Home</a><a>Shop</a><a>Purchase by Weight</a><a>Recipes</a><a>Blog</a>
      <svg class="search" viewBox="0 0 24 24"><circle cx="10" cy="10" r="7" fill="none" stroke="#fff" stroke-width="2.5"/><path d="M15 15l6 6" stroke="#fff" stroke-width="2.5"/></svg>
    </nav>
  </div>
</header>

<section class="hero">
  <div class="hero-photo" role="img" aria-label="Family walking outdoors in a green field under a blue sky"></div>
  <div class="copy">
    <h1>We Create<br>Healthy Food</h1>
    <p>Lorem Ipsum is simply dummy text of the printing and typesetting industry.</p>
    <span class="btn-green">Read More</span>
  </div>
  <svg class="arrow l" viewBox="0 0 30 30"><circle cx="15" cy="15" r="15" fill="#fff" opacity=".85"/><path d="M17 9l-6 6 6 6" fill="none" stroke="#555" stroke-width="2.5"/></svg>
  <svg class="arrow r" viewBox="0 0 30 30"><circle cx="15" cy="15" r="15" fill="#fff" opacity=".85"/><path d="M13 9l6 6-6 6" fill="none" stroke="#555" stroke-width="2.5"/></svg>
</section>

<section class="wrap deals">
  <h2 class="section-title">Latest Deals</h2>
  <div class="products">
    <div class="product">
      <div class="shot" role="img" aria-label="Bowl of fresh ground peanut butter" style="background:linear-gradient(135deg,#c98f4d,#8c5a2a)"></div>
      <h3>Fresh Ground<br>Peanut Butter 380g</h3>
      <div class="price">Now $3.35</div>
      <div class="desc">Freshly ground every week<br>with no added salt.</div>
      <span class="more">Read More</span>
    </div>
    <div class="product">
      <div class="shot" role="img" aria-label="Probiotic supplement jars" style="background:linear-gradient(135deg,#f3ecec,#b8453d)"></div>
      <h3>Inner Balance<br>Plus 60C</h3>
      <div class="price">Now $21.95</div>
      <div class="desc">Daily probiotic support<br>for healthy digestion.</div>
      <span class="more">Read More</span>
    </div>
    <div class="product">
      <div class="shot" role="img" aria-label="Bowl of ground linseed, sunflower and almond meal" style="background:linear-gradient(135deg,#cfc1a4,#9b8a6b)"></div>
      <h3>LSA</h3>
      <div class="price">Now $7.95</div>
      <div class="desc">Linseed, sunflower and<br>almond meal blend.</div>
      <span class="more">Read More</span>
    </div>
    <div class="product">
      <div class="shot" role="img" aria-label="Bowl of fresh ground peanut butter" style="background:linear-gradient(135deg,#c98f4d,#8c5a2a)"></div>
      <h3>Fresh Ground<br>Peanut Butter 380g</h3>
      <div class="price">Now $3.35</div>
      <div class="desc">Freshly ground every week<br>with no added salt.</div>
      <span class="more">Read More</span>
    </div>
  </div>
</section>

<section class="wrap main">
  <div class="news">
    <h2 class="section-title">Latest News</h2>
    <div class="news-item"><div class="text"><h3>History of the almond</h3><p>In history, the almond tree has always been a favourite, and in Shakespeare time an Almond tree was in every garden to use in many dishes and puddings.</p><span class="read">Read More</span></div><div class="thumb" role="img" aria-label="Almonds" style="background:linear-gradient(135deg,#c99a6b,#8a5a32)"></div></div>
    <div class="news-item"><div class="text"><h3>Bliss Balls with Linseed Meal</h3><p>Lorem Ipsum is simply dummy text of the printing and typesetting industry. Lorem Ipsum has been the industry's standard dummy text ever since.</p><span class="read">Read More</span></div><div class="thumb" role="img" aria-label="Bliss balls" style="background:linear-gradient(135deg,#6b4a34,#2e1e14)"></div></div>
    <div class="news-item"><div class="text"><h3>Home Deliveries</h3><p>8/10 Park Road, Greenbrook 2777 &mdash; 12 Market Lane, Ashford Parade 2780 &mdash; 5 Hill Street, Kentwood.</p><span class="read">Read More</span></div><div class="thumb" role="img" aria-label="Delivery box of groceries" style="background:linear-gradient(135deg,#9a9a9a,#4d4d4d)"></div></div>
    <div class="news-item"><div class="text"><h3>Courses</h3><p>Information session on Growing Healthy Cultures and Fermented Foods. Places limited, book at the shop counter.</p><span class="read">Read More</span></div><div class="thumb" role="img" aria-label="Fermented culture grains" style="background:linear-gradient(135deg,#f1ead8,#cdbf9d)"></div></div>
    <div class="news-item"><div class="text"><h3>Courses</h3><p>Information session on Growing Healthy Cultures and Fermented Foods. Places limited, book at the shop counter.</p><span class="read">Read More</span></div><div class="thumb" role="img" aria-label="Fermented culture grains" style="background:linear-gradient(135deg,#e8e0cc,#b9a985)"></div></div>
  </div>
  <aside class="sidebar">
    <div class="side-title">Product Categories</div>
    <ul class="cat">
      <li class="head">Alternative goods</li><li>Bulk Food</li><li>Gluten Free</li><li>Health Supplements</li><li>Natural Beauty</li><li>Organic</li><li>Preserves</li><li>Specials</li><li>Sugar Replacements</li><li>Vegan</li><li>Vegetarian</li>
    </ul>
    <div class="side-title">By Weight Categories</div>
    <ul class="cat">
      <li class="head">Baking</li><li>Beans &amp; Peas</li><li>Candy &amp; Sweet Treats</li><li>Cereals &amp; Granolas</li><li>Coffee &amp; Tea</li><li>Dried Fruit</li><li>Flours</li><li>Fruit Ready Meals</li><li>Gluten Free Processed Meat</li><li>Honey</li><li>Honey Sugar &amp; Natural Replacement</li><li>Nuts</li><li>Oils</li><li>Pasta</li><li>Powder Food</li><li>Protein Food</li><li>Rice</li><li>Seeds</li><li>Specials</li>
    </ul>
  </aside>
</section>

<section class="wrap testimonial">
  <div class="person" role="img" aria-label="Smiling woman in a business jacket"></div>
  <div class="quote">
    <span class="qm open">&ldquo;</span>
    Lorem Ipsum is simply dummy text of the printing and typesetting industry. Lorem Ipsum has been the industry's standard dummy text ever since the 1500s, when an unknown printer took a galley of type and scrambled it to make a type specimen book. It has survived not only five centuries, but also the leap into electronic typesetting.
    <span class="qm close">&rdquo;</span>
  </div>
</section>

<footer class="footer">
  <div class="wrap">
    <div class="fcol"><h4>Latest Content</h4><ul>
      <li>Fresh Ground Peanut Butter 750g</li><li>Fresh Ground Peanut Butter 380g</li><li>Fresh Ground Peanut Butter 250g</li><li>Bliss Balls with Linseed Meal</li><li>History of the almond</li><li>Greenleaf Organic Tamari 500ml</li><li>Greenleaf Organic Unhulled Tahini</li><li>Greenleaf Organic Hulled Tahini</li><li>Ashcombe Organic Lasagna</li><li>Greenleaf Organic Macadamia Oil</li></ul></div>
    <div class="fcol"><h4>About Us</h4><ul>
      <li>Special Orders</li><li>Newsletter</li><li>Welcome to Marlowvale</li><li>Health food Company</li><li>Contact Us</li></ul></div>
    <div class="fcol"><h4>Help</h4><ul>
      <li>Privacy</li><li>Product Recall</li><li>Legals</li><li>Customer Agreement</li></ul></div>
    <div class="fcol"><h4>Newsletter</h4>
      <label>Name</label><div class="field"></div>
      <label>Email</label><div class="field"></div>
      <span class="btn-sub">Submit</span>
    </div>
  </div>
</footer>
<div class="bottombar"><div class="wrap">Copyright &copy; 2014 Marlowvale Wholefoods</div></div>

</body>
</html>
```